Emergency Vehicle Installer and Security Firm Needs a Business Card

Our company "Corvalt" need a business card for our Emergency Vehicle Equipment Installation and Infrastructure Security Business. We are contract designers, manufacturers and installers for Emergency Vehicle Fleets. This includes installation of Emergency Lights, Sirens, Vehicle Graphics and Radio Communications. We also supply this products to an international market. We also do consultant, and installation of high level security access, alarm and surveillance equipment for medium to large size businesses.

The design should represent a level of trust in our professionalism and expertise. It should visually display our ongoing relationship with the emergency services, but not overtake our commitment to high level security options.

Target Market(s)

Emergency Services and Businesses requiring high level security

Industry/Entity Type

Business

Contact Information for Business Card

*note complete details will be given to the winning designer for revising. The name "Mark Pell will be used to fill in name".

Mark Pell
Managing Director
Corvalt NZ Limited
Phone: +64 027 604 91352
Email: mark.pell@corvalt-example.co.nz

Requirements
Must have
• Card must be in black. Using our logo on the top as supplied. Designers should try having the reverse side as a blurred image of police lights (red and blue) with our logo in greyscale in the centre (this is not particularly a requirement, but feel free to play around with this option).
Nice to have
• A card design that looks good when spot UV printed. A clean compact and graphic design. A grey scale feel on the front (excluding logo, but you can play around with that idea). Rounded smooth text.
Should not have
• Will update this section as designs come through - feel free to submit what you feel would look good.

```html
<!DOCTYPE html>
<html lang="en">
<head>
<meta charset="utf-8">
<title>Corvalt Business Card</title>
<link rel="stylesheet" href="https://fonts.googleapis.com/css2?family=Arimo:wght@400;700&display=swap">
<style>
  :root {
    --stage: #7f7f81;
    --card: #0b0b0c;
    --card-edge: #1c1c1e;
    --white: #f4f4f4;
    --red: #e0202a;
  }
  html, body {
    margin: 0;
    padding: 0;
    width: 1200px;
    height: 950px;
    overflow: hidden;
    background: var(--stage);
    font-family: "Arimo", Arial, sans-serif;
  }
  .stage {
    position: relative;
    width: 1200px;
    height: 950px;
  }
  .card {
    position: absolute;
    left: 250px;
    width: 700px;
    height: 400px;
    border-radius: 26px;
    background: var(--card);
    box-shadow: 0 12px 30px rgba(0,0,0,0.35), inset 0 0 0 1px var(--card-edge);
    overflow: hidden;
  }
  .card--front { top: 52px; }
  .card--back { top: 498px; }

  .brand {
    position: absolute;
    right: 60px;
    margin: 0;
    font-size: 62px;
    font-weight: 700;
    letter-spacing: 1px;
    color: var(--white);
    line-height: 1;
  }
  .card--front .brand { top: 176px; }
  .card--back .brand { top: 150px; }

  .contact {
    position: absolute;
    left: 60px;
    top: 118px;
  }
  .contact .name {
    margin: 0;
    font-size: 30px;
    font-weight: 400;
    color: var(--red);
  }
  .contact .role {
    margin: 4px 0 0;
    font-size: 22px;
    color: var(--white);
  }
  .contact .company {
    margin: 62px 0 0;
    font-size: 21px;
    color: var(--red);
  }
  .contact .line {
    margin: 8px 0 0;
    font-size: 18px;
    color: var(--white);
  }
</style>
</head>
<body>
<main class="stage">
  <section class="card card--front" aria-label="Card front">
    <p class="brand">CORVALT</p>
  </section>

  <section class="card card--back" aria-label="Card back">
    <div class="contact">
      <h1 class="name">Mark Pell</h1>
      <p class="role">Managing Director</p>
      <p class="company">Corvalt NZ Limited</p>
      <p class="line">+64 027 604 91352</p>
      <p class="line">mark.pell@corvalt-example.co.nz</p>
    </div>
    <p class="brand">CORVALT</p>
  </section>
</main>
</body>
</html>
```